Business Card Design

My business is writing crime novels to entertain readers. I write legal thrillers and mysteries. I need a card for publishers, agents, other authors, and media.

Industry/Entity Type

Legal

Contact Information for Business Card

Paul Ostrander
www.ostranderthrillers.example
paulbostrander@mailbox.example
0064 27 5139427

```html
<!DOCTYPE html>
<html lang="en">
<head>
<meta charset="utf-8">
<title>Paul Ostrander – Business Card</title>
<link href="https://fonts.googleapis.com/css2?family=Special+Elite&family=Open+Sans:wght@400&display=swap" rel="stylesheet">
<style>
  :root {
    --page-bg: #ecebe8;
    --card-white: #ffffff;
    --paper-light: #b3b6bb;
    --paper-mid: #8d9198;
    --paper-dark: #5a5f67;
    --name-red: #d9262b;
    --ink-dark: #2b2d31;
    --contact-ink: #1e1e1e;
  }
  * { margin: 0; padding: 0; box-sizing: border-box; }
  html, body {
    width: 1200px;
    height: 871px;
    overflow: hidden;
    background: var(--page-bg);
  }
  .business-card {
    position: absolute;
    left: 100px;
    top: 151px;
    width: 1000px;
    height: 568px;
    background: var(--card-white);
    box-shadow: 0 6px 24px rgba(0, 0, 0, 0.12);
  }
  .paper-panel {
    position: absolute;
    left: 25px;
    top: 6px;
    width: 950px;
    height: 450px;
    background:
      radial-gradient(ellipse at 75% 20%, var(--paper-light) 0%, transparent 60%),
      radial-gradient(ellipse at 15% 90%, var(--paper-dark) 0%, transparent 55%),
      linear-gradient(160deg, var(--paper-mid) 0%, #7c8088 55%, var(--paper-dark) 100%);
  }
  .author-name {
    position: absolute;
    left: 62px;
    top: 190px;
    font-family: "Special Elite", "Courier New", monospace;
    font-size: 96px;
    line-height: 1;
    color: var(--name-red);
    white-space: nowrap;
  }
  .author-website {
    position: absolute;
    right: 72px;
    top: 332px;
    font-family: "Special Elite", "Courier New", monospace;
    font-size: 36px;
    line-height: 1;
    color: var(--ink-dark);
    white-space: nowrap;
  }
  .contact-strip {
    position: absolute;
    left: 45px;
    right: 45px;
    top: 476px;
    display: flex;
    justify-content: space-between;
    font-family: "Open Sans", Arial, sans-serif;
    font-size: 30px;
    line-height: 1.3;
    color: var(--contact-ink);
    white-space: nowrap;
  }
</style>
</head>
<body>
  <div class="business-card">
    <div class="paper-panel" role="img" aria-label="Crumpled grey paper texture"></div>
    <h1 class="author-name">Paul Ostrander</h1>
    <p class="author-website">www.ostranderthrillers.example</p>
    <div class="contact-strip">
      <span class="contact-email">paulbostrander@mailbox.example</span>
      <span class="contact-phone">0064 27 5139427</span>
    </div>
  </div>
</body>
</html>
```